Pagewall, Blipster and Crewnest cover image design

Looking to update the pagewall, blipster and aLinkedin cover images for Halvard Ledger . website www.halvledger-example.com
https://www.crewnest-example.com/company/halvard-ledger-llc/mycompany/?viewAsMember=true
https://www.pagewall-example.com/halvledger
https://blipster-example.com/halvledger

```html
<!DOCTYPE html>
<html lang="en">
<head>
<meta charset="utf-8">
<title>Halvard Ledger — Social Cover Set</title>
<link rel="stylesheet" href="https://fonts.googleapis.com/css2?family=Poppins:ital,wght@0,400;0,500;0,600;0,700;1,700&display=swap">
<style>
  :root {
    --board: #444444;
    --board-glow: #4d4d4d;
    --label: #f2f2f2;
    --green: #4b8c40;
    --orange: #f0620c;
    --ink: #2a2a2a;
    --white: #ffffff;
    --photo-deep: #86b752;
    --photo-mid: #b7d48c;
    --photo-light: #e2ecd2;
  }
  * { box-sizing: border-box; margin: 0; padding: 0; }
  html, body { width: 1200px; height: 1180px; overflow: hidden; }
  body {
    background: radial-gradient(ellipse at center, var(--board-glow) 0%, var(--board) 70%);
    font-family: 'Poppins', sans-serif;
    position: relative;
  }
  .platform-label {
    position: absolute; left: 0; width: 1200px; text-align: center;
    color: var(--label); font-size: 18px; font-weight: 500;
  }
  .banner { position: absolute; background: var(--green); overflow: hidden; }
  .banner__photo {
    position: absolute; left: 0; top: 0; width: 100%;
    background: linear-gradient(90deg, var(--photo-deep) 0%, var(--photo-mid) 30%, #c9b679 42%, var(--photo-light) 55%, var(--white) 68%);
  }
  .brand { position: absolute; display: flex; align-items: center; gap: 3px; }
  .brand__mark { background: var(--green); display: block; }
  .brand__name {
    color: var(--ink); font-weight: 700; line-height: 0.95; text-transform: uppercase; letter-spacing: -0.02em;
  }
  .headline {
    position: absolute; text-align: right; font-weight: 600; line-height: 1.15; color: var(--ink); letter-spacing: -0.01em;
  }
  .headline__accent { color: var(--orange); font-weight: 700; display: block; }
  .headline__accent em { font-style: italic; }
  .tab {
    position: absolute; left: 0; background: var(--orange); color: var(--white); font-weight: 700;
    display: flex; align-items: center; text-transform: uppercase;
    clip-path: polygon(0 0, calc(100% - 14px) 0, 100% 50%, calc(100% - 14px) 100%, 0 100%);
  }
  .industry-list { position: absolute; list-style: none; color: var(--white); font-weight: 500; white-space: nowrap; }
  .industry-list li { display: flex; align-items: flex-start; }
  .industry-list svg { flex: none; }
  .call-bar {
    position: absolute; right: 0; background: var(--orange); color: var(--white); font-weight: 500;
    display: flex; align-items: center; white-space: nowrap;
    clip-path: polygon(12px 0, 100% 0, 100% 100%, 12px 100%, 0 50%);
  }

  /* Pagewall cover */
  .banner--pagewall { left: 350px; top: 141px; width: 500px; height: 191px; }
  .banner--pagewall .banner__photo { height: 109px; }
  .banner--pagewall .brand { left: 410px; top: 4px; }
  .banner--pagewall .brand__mark { width: 21px; height: 21px; }
  .banner--pagewall .brand__name { font-size: 8px; }
  .banner--pagewall .headline { right: 8px; top: 41px; font-size: 19px; }
  .banner--pagewall .tab { top: 95px; width: 146px; height: 27px; padding-left: 8px; font-size: 12px; }
  .banner--pagewall .industry-list { top: 134px; font-size: 9px; }
  .banner--pagewall .industry-list li { height: 17.5px; gap: 4px; }
  .banner--pagewall .industry-list svg { width: 11px; height: 11px; }
  .banner--pagewall .list-a { left: 8px; }
  .banner--pagewall .list-b { left: 214px; }
  .banner--pagewall .list-c { left: 329px; top: 133px; font-size: 8.3px; line-height: 1.45; }
  .banner--pagewall .list-c li { height: auto; }
  .banner--pagewall .call-bar { top: 162px; width: 178px; height: 20px; padding-left: 17px; font-size: 13px; }

  /* Blipster cover */
  .banner--blipster { left: 143px; top: 428px; width: 914px; height: 305px; }
  .banner--blipster .banner__photo { height: 157px; }
  .banner--blipster .brand { left: 786px; top: 10px; gap: 4px; }
  .banner--blipster .brand__mark { width: 32px; height: 32px; }
  .banner--blipster .brand__name { font-size: 13px; }
  .banner--blipster .headline { right: 8px; top: 60px; font-size: 35px; line-height: 1.2; }
  .banner--blipster .tab { top: 134px; width: 270px; height: 52px; padding-left: 11px; font-size: 23px; }
  .banner--blipster .industry-list { top: 206px; font-size: 17px; }
  .banner--blipster .industry-list li { height: 32.5px; gap: 8px; }
  .banner--blipster .industry-list svg { width: 21px; height: 21px; margin-top: 2px; }
  .banner--blipster .list-a { left: 9px; }
  .banner--blipster .list-b { left: 390px; }
  .banner--blipster .list-c { left: 604px; top: 205px; font-size: 16px; line-height: 1.4; }
  .banner--blipster .list-c li { height: auto; gap: 5px; }
  .banner--blipster .call-bar { top: 257px; width: 320px; height: 39px; padding-left: 31px; font-size: 25px; }

  /* Crewnest cover */
  .banner--crewnest { left: 113px; top: 825px; width: 971px; height: 241px; }
  .banner--crewnest .banner__photo { height: 139px;
    background: linear-gradient(90deg, var(--photo-mid) 0%, var(--photo-deep) 25%, #c9b679 45%, var(--photo-light) 58%, var(--white) 70%); }
  .banner--crewnest .brand { left: 836px; top: 15px; gap: 4px; }
  .banner--crewnest .brand__mark { width: 30px; height: 30px; }
  .banner--crewnest .brand__name { font-size: 12px; }
  .banner--crewnest .headline { right: 34px; top: 56px; font-size: 31px; line-height: 1.1; }
  .banner--crewnest .tab { left: 246px; top: 126px; width: 151px; height: 28px; padding-left: 12px; font-size: 12.5px; }
  .banner--crewnest .industry-list { top: 163px; font-size: 12px; }
  .banner--crewnest .industry-list li { height: 20.5px; gap: 4px; }
  .banner--crewnest .industry-list svg { width: 12px; height: 12px; margin-top: 2px; }
  .banner--crewnest .list-a { left: 248px; }
  .banner--crewnest .list-b { left: 544px; }
  .banner--crewnest .list-c { left: 736px; line-height: 1.2; }
  .banner--crewnest .list-c li { height: auto; }
  .banner--crewnest .call-bar { top: 201px; width: 226px; height: 25px; padding-left: 17px; font-size: 14px; }
</style>
</head>
<body>
<svg width="0" height="0" style="position:absolute" aria-hidden="true">
  <symbol id="tick-box" viewBox="0 0 20 20">
    <rect x="1.5" y="4" width="14" height="14" rx="2" fill="none" stroke="#fff" stroke-width="2"/>
    <path d="M5 10.5 L9 14.5 L18.5 3" fill="none" stroke="#fff" stroke-width="2.6" stroke-linecap="round" stroke-linejoin="round"/>
  </symbol>
</svg>

<p class="platform-label" style="top:95px">Pagewall</p>
<section class="banner banner--pagewall">
  <div class="banner__photo" role="img" aria-label="Photo of seedlings growing from stacks of gold coins on a soft green background"></div>
  <div class="brand"><span class="brand__mark"></span><span class="brand__name">Halvard<br>Ledger</span></div>
  <h1 class="headline">INCREASE CASH FLOW,<span class="headline__accent"><em>GROW</em> YOUR BUSINESS!</span></h1>
  <div class="tab">Industries Served</div>
  <ul class="industry-list list-a">
    <li><svg><use href="#tick-box"/></svg>Automotive/Truck Dealerships</li>
    <li><svg><use href="#tick-box"/></svg>Repair Shops &amp; Parts Distributors</li>
    <li><svg><use href="#tick-box"/></svg>Industrial Maintenance Transportation</li>
  </ul>
  <ul class="industry-list list-b">
    <li><svg><use href="#tick-box"/></svg>Staffing</li>
    <li><svg><use href="#tick-box"/></svg>Transportation</li>
    <li><svg><use href="#tick-box"/></svg>Oil &amp; Gas</li>
  </ul>
  <ul class="industry-list list-c">
    <li><svg><use href="#tick-box"/></svg><span>Storm Response, Utility Restoration<br>and Maintenance Services</span></li>
  </ul>
  <div class="call-bar">Call us:&nbsp; 555.010.4821</div>
</section>

<p class="platform-label" style="top:390px">Blipster</p>
<section class="banner banner--blipster">
  <div class="banner__photo" role="img" aria-label="Photo of seedlings growing from stacks of gold coins on a soft green background"></div>
  <div class="brand"><span class="brand__mark"></span><span class="brand__name">Halvard<br>Ledger</span></div>
  <h2 class="headline">INCREASE CASH FLOW,<span class="headline__accent"><em>GROW</em> YOUR BUSINESS!</span></h2>
  <div class="tab">Industries Served</div>
  <ul class="industry-list list-a">
    <li><svg><use href="#tick-box"/></svg>Automotive/Truck Dealerships</li>
    <li><svg><use href="#tick-box"/></svg>Repair Shops &amp; Parts Distributors</li>
    <li><svg><use href="#tick-box"/></svg>Industrial Maintenance Transportation</li>
  </ul>
  <ul class="industry-list list-b">
    <li><svg><use href="#tick-box"/></svg>Staffing</li>
    <li><svg><use href="#tick-box"/></svg>Transportation</li>
    <li><svg><use href="#tick-box"/></svg>Oil &amp; Gas</li>
  </ul>
  <ul class="industry-list list-c">
    <li><svg><use href="#tick-box"/></svg><span>Storm Response, Utility Restoration<br>and Maintenance Services</span></li>
  </ul>
  <div class="call-bar">Call us:&nbsp; 555.010.4821</div>
</section>

<p class="platform-label" style="top:779px">crewnest</p>
<section class="banner banner--crewnest">
  <div class="banner__photo" role="img" aria-label="Photo of seedlings growing from stacks of gold coins on a soft green background"></div>
  <div class="brand"><span class="brand__mark"></span><span class="brand__name">Halvard<br>Ledger</span></div>
  <h2 class="headline">INCREASE CASH FLOW,<span class="headline__accent"><em>GROW</em> YOUR BUSINESS!</span></h2>
  <div class="tab">Industries Served</div>
  <ul class="industry-list list-a">
    <li><svg><use href="#tick-box"/></svg>Automotive/Truck Dealerships</li>
    <li><svg><use href="#tick-box"/></svg>Repair Shops &amp; Parts Distributors</li>
    <li><svg><use href="#tick-box"/></svg>Industrial Maintenance Transportation</li>
  </ul>
  <ul class="industry-list list-b">
    <li><svg><use href="#tick-box"/></svg>Staffing</li>
    <li><svg><use href="#tick-box"/></svg>Transportation</li>
    <li style="font-size:10px"><svg><use href="#tick-box"/></svg>Oil &amp; Gas</li>
  </ul>
  <ul class="industry-list list-c">
    <li><svg><use href="#tick-box"/></svg><span>Storm Response, Utility Restoration<br>and Maintenance Services</span></li>
  </ul>
  <div class="call-bar">Call us:&nbsp; 555.010.4821</div>
</section>
</body>
</html>
```